Postcard for Antique Furniture Restorer

My business is to restore antique furniture. I am based in Sydney, Australia.

I will be using this postcard to promote my business.
I will give it to customers like a With Compliments card.

Sometimes I will be writing information on the back of the card.

Design for Postcard Size eg 148 X 105mm

Front of card:

Attached are images of Antique furniture - please use ONLY 1 of the 3 images.
Deep etch the image on a white or cream background.

On front of card add these words:
Timber Reborn
antique furniture restoration

Antiques travel through time, seeing generations of families
Through time they remain - they tell a continuing story
Be part of the journey

Back of postcard:
(leave space for notes to be handwritten)

Add these words:

Timber Reborn
Corin Maddox
mobile 0437 552 618
www.oakandvarnishcraft.com.au

Industry/Entity Type

Business

Font styles to use
Serif
Sans Serif

Colors
fefdec
ffffff

Requirements
Must have
• Use only 1 image. Image must be deep etched.

```html
<!DOCTYPE html>
<html lang="en">
<head>
<meta charset="utf-8">
<title>Timber Reborn – antique furniture restoration postcard</title>
<link rel="stylesheet" href="https://fonts.googleapis.com/css2?family=Arimo:wght@400&display=swap">
<style>
  :root {
    --cream-top: #f6f0dc;
    --cream-bottom: #fefdec;
    --panel-fill: rgba(255, 255, 255, 0.45);
    --panel-line: #b9b09c;
    --ink: #1f1f1f;
    --band-top: #6c5c4a;
    --band-bottom: #3d2d1c;
    --band-text: #f8f4ea;
    --wood-light: #9a4a22;
    --wood-mid: #6e321a;
    --wood-dark: #3f1e10;
  }
  * { margin: 0; padding: 0; box-sizing: border-box; }
  html, body { width: 1200px; height: 884px; overflow: hidden; }
  body { font-family: "Arimo", Arial, sans-serif; }

  .postcard {
    position: relative;
    width: 1200px;
    height: 884px;
    background: linear-gradient(180deg, var(--cream-top) 0%, var(--cream-bottom) 70%);
    overflow: hidden;
  }

  .brand-panel {
    position: absolute;
    left: 0;
    top: 248px;
    width: 661px;
    height: 151px;
    background: var(--panel-fill);
    border: 1px solid var(--panel-line);
    border-left: none;
    padding: 29px 0 0 27px;
    color: var(--ink);
  }
  .brand-name,
  .brand-tagline {
    font-size: 39px;
    font-weight: 400;
    line-height: 45px;
  }

  .story-band {
    position: absolute;
    left: 0;
    top: 619px;
    width: 1200px;
    height: 265px;
    background: linear-gradient(180deg, var(--band-top) 0%, var(--band-bottom) 100%);
  }
  .story-lines {
    position: absolute;
    right: 91px;
    top: 77px;
    text-align: right;
    color: var(--band-text);
    font-size: 39px;
    line-height: 45px;
    list-style: none;
    white-space: nowrap;
  }

  .armoire-photo {
    position: absolute;
    left: 764px;
    top: 122px;
    width: 375px;
    height: 548px;
    z-index: 2;
    background: linear-gradient(135deg, var(--wood-dark) 0%, var(--wood-light) 45%, var(--wood-mid) 75%, var(--wood-dark) 100%);
    box-shadow: 6px 6px 10px rgba(0, 0, 0, 0.3);
  }
</style>
</head>
<body>
  <main class="postcard">
    <section class="brand-panel">
      <h1 class="brand-name">Timber Reborn</h1>
      <p class="brand-tagline">antique furniture restoration</p>
    </section>

    <div class="armoire-photo" role="img" aria-label="Deep-etched photograph of a carved antique French armoire with burl wood double doors"></div>

    <section class="story-band">
      <ul class="story-lines">
        <li>Antiques travel through time, seeing generations of families</li>
        <li>Through time they remain~they tell a continuing story</li>
        <li>Be part of the Journey</li>
      </ul>
    </section>
  </main>
</body>
</html>
```